Association qui souhaite améliorer l'accès aux personnes en situation de handicap

Nous sommes une association qui a pour objectif d'améliorer l'accessibilité, augmenter l'offre des activités réalisables dans notre région touristique.
Nous souhaitons réaliser un site internet afin de pouvoir communiquer sur notre association. Nous avons déjà conçu notre flyer sur Graphivolte. Nous souhaiterions une base graphique se rapportant à celui-ci. C'est possible de tout retravailler mais nous souhaitons tout de même retrouver la charte graphique ou code couleur du flyer.
Il nous faudrait quelques pages:
- 1 page : Acceuil / Présentation (Home), Il y aurait le descriptif de l'association, avec ses objectifs à +/- moyen terme
- 1 page : Nos réalisations, celle-ci présenterait les éléments que nous avons réalisés avec des zones de textes et des images classées chronologiquement au fur et à mesure des nouveautés
- 1 page : Media, comme la précédente, mais ou on pourrait voir ou lire sur les divers médias qui parlent de nous
- 1 page : Evenements : c'est une page pour présenter divers activités que nous allons organiser
- 1 page : Contact qui indique comment nous contacter et avec la présentation des 5 ou 6 membres du comité
- 1 link donate : qui arrive sur un formulaire de donnée que l'on pourra faire évoluer sur un système de payement par la suite. Cette bannière doit se retrouver sur toutes les pages
Il est nécessaire que se design puisse être transféré sur une lecture sur téléphone mobile
Personnes en situation de handicap
Associatif
Coded - Design and coding required
5+ page

```html
<!DOCTYPE html>
<html lang="en">
<head>
<meta charset="utf-8">
<title>Pathway Open Association</title>
<link href="https://fonts.googleapis.com/css2?family=Bebas+Neue&family=Raleway:wght@400;500;600;700&display=swap" rel="stylesheet">
<style>
:root{
  --red:#e3201f;
  --red-dark:#b0151a;
  --ink:#2c3138;
  --text:#6b6f75;
  --grey-bg:#f6f6f6;
  --footer:#1e1f22;
  --white:#ffffff;
}
*{box-sizing:border-box;margin:0;padding:0}
html,body{width:1200px;height:4691px;overflow:hidden}
body{font-family:"Raleway",sans-serif;color:var(--text);background:var(--white);position:relative}
.heading{font-family:"Bebas Neue",sans-serif;font-weight:400;color:var(--ink);letter-spacing:.5px;line-height:1.05}
.heading .accent{color:var(--red)}

/* header */
.site-header{position:absolute;top:0;left:0;width:1200px;height:113px;background:var(--white);z-index:5}
.brand{position:absolute;left:110px;top:26px;display:flex;align-items:center;gap:12px}
.brand-mark{width:48px;height:48px;background:var(--red)}
.brand-name{font-family:"Raleway",sans-serif;font-weight:700;font-size:22px;line-height:1.05;color:var(--ink);text-transform:uppercase}
.top-mail{position:absolute;right:110px;top:22px;font-size:17px;color:var(--ink);display:flex;align-items:center;gap:7px}
.main-nav{position:absolute;right:110px;top:73px;display:flex;gap:26px;font-size:17px;font-weight:600;color:var(--ink);text-transform:uppercase}
.main-nav .active{color:var(--red)}

/* hero */
.hero{position:absolute;top:113px;left:0;width:1200px;height:800px}
.hero-photo{position:absolute;inset:0;background:linear-gradient(110deg,#d9dbd8 0%,#c4c7bd 30%,#8c9a6a 55%,#58663a 78%,#34352e 100%)}
.hero-shape{position:absolute;inset:0}
.hero-title{position:absolute;left:110px;top:120px;font-size:62px;color:var(--white)}
.btn{display:inline-block;border-radius:40px;font-family:"Raleway",sans-serif;font-weight:600;text-transform:uppercase}
.btn-light{background:var(--white);color:var(--ink)}
.btn-red{background:var(--red);color:var(--white)}
.hero .btn{position:absolute;left:112px;top:292px;padding:21px 26px;font-size:19px}

/* welcome */
.welcome-photo{position:absolute;left:65px;top:900px;width:555px;height:385px;border-radius:6px;background:linear-gradient(135deg,#a9b9c6 0%,#8ea0a8 35%,#6f7f6a 65%,#8a8f88 100%)}
.welcome-text{position:absolute;left:668px;top:980px;width:440px}
.welcome-text .heading{font-size:44px}
.welcome-text p{font-size:15.5px;line-height:1.75;margin-top:26px}
.welcome-text .members{font-size:17px;color:var(--ink);margin-top:20px;line-height:1.75}
.welcome-text .btn{margin-top:30px;padding:16px 20px;font-size:17px}

/* projects */
.projects{position:absolute;top:1440px;left:0;width:1200px;height:610px;background:var(--grey-bg)}
.projects-art{position:absolute;right:0;top:-4px;width:660px;height:614px}
.projects .heading{position:absolute;left:110px;top:70px;font-size:44px}
.project-list{position:absolute;left:110px;top:150px;width:500px;list-style:none}
.project-list li{position:relative;padding-left:25px;font-size:15.5px;line-height:1.8;margin-bottom:22px}
.project-list li::before{content:"";position:absolute;left:0;top:6px;width:14px;height:14px;border-radius:50%;background:var(--red)}
.project-list li::after{content:"";position:absolute;left:4px;top:9px;width:5px;height:3px;border-left:2px solid #fff;border-bottom:2px solid #fff;transform:rotate(-45deg)}

/* events */
.section-title{position:absolute;left:0;width:1200px;text-align:center;font-size:44px}
.event-card{position:absolute;top:2190px;width:312px}
.event-photo{width:312px;height:245px}
.event-card h3{font-weight:500;font-size:21px;color:var(--ink);margin-top:24px}
.event-meta{font-size:15px;margin-top:10px;color:var(--text)}
.event-meta .ico{display:inline-block;width:12px;height:12px;background:var(--red);margin-right:4px;vertical-align:-1px;border-radius:2px}
.event-card p{font-size:15px;line-height:1.75;margin-top:24px}
.event-card .more{display:block;margin-top:22px;font-size:15px;font-weight:600;color:var(--red);text-transform:uppercase}

/* rejoin */
.rejoin{position:absolute;top:2722px;left:0;width:1200px;height:506px}
.rejoin-photo{position:absolute;inset:0;background:linear-gradient(180deg,#3d5660 0%,#6a7f78 35%,#c79a4d 58%,#d98a2c 70%,#a7631f 100%)}
.rejoin .heading{position:absolute;left:111px;top:58px;font-size:44px;color:var(--white)}
.rejoin p{position:absolute;left:112px;top:130px;width:560px;font-size:15.5px;line-height:1.75;color:var(--white)}
.tier{position:absolute;top:203px;width:242px;height:242px;border-radius:50%;background:var(--white);text-align:center;padding-top:50px}
.tier h4{font-weight:500;font-size:23px;color:var(--ink);line-height:1.25}
.tier .price{font-size:15px;margin-top:20px;line-height:1.75;color:var(--text)}
.tier .price b{color:var(--ink)}

/* contact */
.contact-photo{position:absolute;left:111px;top:3385px;width:391px;height:398px}
.contact-form{position:absolute;left:580px;top:3385px;width:510px}
.field{border-bottom:1px solid #9a9ea3;height:62px;font-size:16.5px;color:var(--ink);padding-top:2px}
.field.message{height:140px;padding-top:24px}
.field + .field{padding-top:24px}
.contact-form .btn{margin-top:33px;padding:15px 25px;font-size:18px}

/* donate */
.donate{position:absolute;top:3858px;left:0;width:1200px;height:520px}
.donate-photo{position:absolute;inset:0;background:linear-gradient(120deg,#d8261f 0%,#e84b36 40%,#c81d1c 70%,#e3413a 100%)}
.donate .heading{position:absolute;top:40px;width:1200px;text-align:center;font-size:44px;color:var(--white)}
.donate p{position:absolute;top:115px;left:250px;width:700px;text-align:center;font-size:15.5px;line-height:1.75;color:var(--white)}
.donate .btn{position:absolute;left:508px;top:192px;padding:16px 30px;font-size:17px}

/* footer */
.site-footer{position:absolute;top:4060px;left:0;width:1200px;height:631px}
.footer-shape{position:absolute;inset:0}
.footer-brand{position:absolute;left:116px;top:370px;display:flex;align-items:center;gap:12px}
.footer-brand .brand-mark{background:var(--white)}
.footer-brand .brand-name{color:var(--white);font-size:24px}
.footer-col{position:absolute;top:302px;color:var(--white)}
.footer-col h5{font-weight:600;font-size:19px;margin-bottom:26px}
.footer-col li{list-style:none;font-size:16px;line-height:32px}
.footer-col .pin,.footer-col .mail{display:inline-block;width:10px;height:12px;background:var(--red);margin-right:8px}
.footer-col .pin{border-radius:50% 50% 50% 0;transform:rotate(-45deg)}
.footer-rule{position:absolute;left:110px;top:565px;width:980px;height:1px;background:#444649}
.copyright{position:absolute;left:110px;top:592px;font-size:16px;color:var(--white)}
</style>
</head>
<body>

<header class="site-header">
  <div class="brand"><span class="brand-mark"></span><span class="brand-name">Pathway Open<br>Association</span></div>
  <div class="top-mail"><svg width="16" height="12" viewBox="0 0 16 12"><rect width="16" height="12" rx="1" fill="#e3201f"/><path d="M1 1l7 6 7-6" stroke="#fff" stroke-width="1.5" fill="none"/></svg>info@pathwayopen-asso.ch</div>
  <nav class="main-nav"><span class="active">Home</span><span>Achievements</span><span>Media</span><span>Events</span><span>Contact</span></nav>
</header>

<section class="hero">
  <div class="hero-photo" role="img" aria-label="Photo of a person in a wheelchair touching tall grass in a sunny field"></div>
  <svg class="hero-shape" viewBox="0 0 1200 800" width="1200" height="800">
    <polygon points="0,452 738,792 1200,570 1200,800 0,800" fill="#fff"/>
    <polygon points="40,430 770,610 660,680" fill="#b0151a" opacity=".9"/>
    <polygon points="745,800 1200,575 1200,650 770,800" fill="#e3201f"/>
  </svg>
  <h1 class="heading hero-title">Improve access for<br>people with disabilities</h1>
  <a class="btn btn-light">Donate now!</a>
</section>

<div class="welcome-photo" role="img" aria-label="Photo of a person walking with a white cane along a lakeside path"></div>
<div class="welcome-text">
  <h2 class="heading">Welcome to<br><span class="accent">Pathway Open Association</span></h2>
  <p>Friends living in the region who are committed to making the Dents du Midi region as accessible as possible to people with disabilities.</p>
  <p class="members">Lucien Morand - Elise Varin - Dubois - Nadia Ferrat - Paul Varin - Dubois - Timo Reynard</p>
  <a class="btn btn-red">Read more</a>
</div>

<section class="projects">
  <svg class="projects-art" viewBox="0 0 660 614" role="img" aria-label="Photo of a smiling mother and child close together">
    <defs><linearGradient id="pg" x1="0" y1="0" x2="1" y2="1"><stop offset="0" stop-color="#8a6b55"/><stop offset=".5" stop-color="#c9a38a"/><stop offset="1" stop-color="#6f7552"/></linearGradient></defs>
    <path d="M0,4 L660,0 L660,614 C560,570 460,560 360,540 C200,500 190,300 120,180 C80,100 30,40 0,4Z" fill="#e3201f"/>
    <path d="M0,4 L660,0 L660,585 C560,545 460,535 370,515 C220,475 205,290 135,170 C90,95 40,40 0,4Z" fill="url(#pg)"/>
  </svg>
  <h2 class="heading">Projects of <span class="accent">the association</span></h2>
  <ul class="project-list">
    <li>Promote the reception and leisure of people with disabilities in the Dents du Midi region by grouping information</li>
    <li>Serve the general interest of people with disabilities as well as relieve caregivers and accompanying persons.</li>
    <li>Allow access to leisure and places like everyone else.</li>
    <li>Raising awareness and developing social representations, through actions, communications, projects and events affecting and involving associative, economic, political partners, the media and the general public.</li>
    <li>Promote collaboration with local actors.</li>
  </ul>
</section>

<h2 class="heading section-title" style="top:2110px">Latest <span class="accent">events</span></h2>
<article class="event-card" style="left:111px">
  <div class="event-photo" role="img" aria-label="Photo of a mother carrying her laughing daughter on her back" style="background:linear-gradient(135deg,#4f7a2a,#a8c24f 50%,#3d5c22)"></div>
  <h3>Finibus Bonoruet Malorum</h3>
  <div class="event-meta"><span class="ico"></span>13/06/2022 &nbsp;|&nbsp; <span class="ico"></span>Admin</div>
  <p>Nam libero tempore, cum soluta nobis est eligendi optio cumque nihil impedit quo minus id quod maxi.</p>
  <span class="more">Read more</span>
</article>
<article class="event-card" style="left:444px">
  <div class="event-photo" role="img" aria-label="Photo of a child in a wheelchair raising her arms in an autumn field" style="background:linear-gradient(180deg,#d9b9a8,#c7906a 45%,#8a7a3a)"></div>
  <h3>Finibus Bonoruet Malorum</h3>
  <div class="event-meta"><span class="ico"></span>13/06/2022 &nbsp;|&nbsp; <span class="ico"></span>Admin</div>
  <p>Nam libero tempore, cum soluta nobis est eligendi optio cumque nihil impedit quo minus id quod maxi.</p>
  <span class="more">Read more</span>
</article>
<article class="event-card" style="left:777px">
  <div class="event-photo" role="img" aria-label="Close-up photo of a human eye" style="background:linear-gradient(160deg,#f1e3da,#d9b8a6 50%,#b88c72)"></div>
  <h3>Finibus Bonoruet Malorum</h3>
  <div class="event-meta"><span class="ico"></span>13/06/2022 &nbsp;|&nbsp; <span class="ico"></span>Admin</div>
  <p>Nam libero tempore, cum soluta nobis est eligendi optio cumque nihil impedit quo minus id quod maxi.</p>
  <span class="more">Read more</span>
</article>

<section class="rejoin">
  <div class="rejoin-photo" role="img" aria-label="Photo of a person in a wheelchair holding balloons on a beach at sunset"></div>
  <h2 class="heading">Rejoin the association</h2>
  <p>The resources of the association come from subscriptions, donations and events organized throughout the year. Annual membership fee:</p>
  <div class="tier" style="left:113px">
    <h4>Associate<br>Member</h4>
    <div class="price"><b>CHF 35.-</b> per person/year<br><b>CHF 60.-</b> per couple/year</div>
  </div>
  <div class="tier" style="left:381px">
    <h4>Benefactor<br>Member</h4>
    <div class="price"><b>CHF 100.-</b> /year</div>
  </div>
</section>

<h2 class="heading section-title" style="top:3298px">Contact <span class="accent">us</span></h2>
<div class="contact-photo" role="img" aria-label="Photo of a man walking with a white cane between trees" style="background:linear-gradient(90deg,#5c7a3a,#d8d6c8 40%,#e08a5a 50%,#d8d6c8 62%,#5f7e3c)"></div>
<form class="contact-form">
  <div class="field">Name</div>
  <div class="field">Email</div>
  <div class="field">Phone No</div>
  <div class="field message">Message</div>
  <a class="btn btn-red">Submit</a>
</form>

<section class="donate">
  <div class="donate-photo" role="img" aria-label="Photo of two people holding hands, tinted red"></div>
  <h2 class="heading">Donate</h2>
  <p>Nemo enim ipsam voluptatem quia voluptas sit aspernatur aut odit aut fugit, sed quia co nsequuntur magni dolores eos qui ratione voluptatem sequi nesciunt.</p>
  <a class="btn btn-light">Donate now</a>
</section>

<footer class="site-footer">
  <svg class="footer-shape" viewBox="0 0 1200 631" width="1200" height="631">
    <polygon points="0,280 470,100 1200,300 1200,631 0,631" fill="#1e1f22"/>
    <polygon points="0,300 440,118 470,100 0,320" fill="#e3201f"/>
  </svg>
  <div class="footer-brand"><span class="brand-mark"></span><span class="brand-name">Pathway Open<br>Association</span></div>
  <div class="footer-col" style="left:512px">
    <h5>Quick Links</h5>
    <ul><li>Home</li><li>Achievements</li><li>Media</li><li>Events</li><li>Contact</li></ul>
  </div>
  <div class="footer-col" style="left:700px">
    <h5>Contact Us</h5>
    <ul><li>Pathway Open Association</li><li><span class="pin"></span>Chemin des Tilleuls 12 1870 Montval</li><li><span class="mail"></span>info@pathwayopen-asso.ch</li></ul>
  </div>
  <div class="footer-rule"></div>
  <div class="copyright">Copyright © 2022, Pathway Open Association. All rights reserved.</div>
</footer>

</body>
</html>
```